Brochure design for joint venture

We need a 4 page A4 brochure for a joing venture between two engineering companies.A draft version of the text can be found in the attachments, along with the logo. The text pdf shows the general style and layout of hte text, but am very open to artistic advice.Image placeholders should be added on pages indicated - these are not yet availableColour scheme is orange and green, looking for strong, bold, lines. Look and feel should be clean and professional, not too cluttered.Final desing shoul dbe avialable in RGB psd format, with full layers so we can modify text and images easily.
Like the look of this style:
https://www.plarnivo.com/vector-art/483921-orange-and-green-business-brochure-design-template

```html
<!DOCTYPE html>
<html lang="en">
<head>
<meta charset="utf-8">
<title>Veltrion &amp; Thermalis Drives – Partnership Brochure</title>
<link href="https://fonts.googleapis.com/css2?family=Oswald:wght@500;600;700&family=Roboto+Condensed:wght@400;700&family=Lato:wght@400;700&display=swap" rel="stylesheet">
<style>
:root{
  --stage:#8e8e8e;
  --orange:#ee7a1c;
  --orange-deep:#d8650e;
  --orange-ink:#dd6a12;
  --green:#3faa4f;
  --green-soft:#58bd5f;
  --ink:#333;
  --white:#fff;
  --head:'Oswald',sans-serif;
  --cond:'Roboto Condensed',sans-serif;
  --body:'Lato',sans-serif;
}
*{box-sizing:border-box;margin:0;padding:0}
html,body{width:1200px;height:1200px;overflow:hidden;background:var(--stage)}
.spread{position:relative;width:1200px;height:1200px}
.page{position:absolute;width:378px;height:530px;background:var(--white);overflow:hidden;box-shadow:4px 10px 14px rgba(0,0,0,.35);font-family:var(--body);color:var(--ink)}
.p-cover{left:162px;top:46px;background:var(--orange)}
.p-intro{left:597px;top:46px}
.p-expertise{left:162px;top:637px}
.p-why{left:596px;top:637px}
.abs{position:absolute}
.photo{position:absolute}

/* cover */
.cover-photo{inset:0;background:radial-gradient(circle at 40% 35%,#f6a25a 0%,#ee7a1c 45%,#d8650e 100%)}
.brand-main{left:0;right:0;top:242px;text-align:center;color:var(--white);font-family:var(--head);font-weight:600;font-size:22px;letter-spacing:1px}
.brand-main small{display:block;font-size:8px;letter-spacing:3px;font-weight:600;margin-top:2px}
.brand-second{left:248px;top:418px;color:var(--white);font-family:var(--body);font-weight:400;font-size:17px;display:flex;align-items:center;gap:6px}
.brand-second i{width:10px;height:10px;border:1.5px solid var(--white);border-radius:50%}
.contact-lead{left:29px;top:434px;color:var(--white);font-size:7.4px;line-height:1.4}
.contact-lead b{font-weight:700}
.contact-list{top:467px;color:var(--white);font-size:7.6px;line-height:2;list-style:none}
.contact-list li{display:flex;align-items:center;gap:5px}
.contact-list.mail{left:29px}
.contact-list.web{left:236px}
.ic{width:8px;height:6px;background:#fde3cc;border-radius:1px;flex:none}
.ic.globe{width:7px;height:7px;border-radius:50%;background:none;border:1.2px solid #fff3e8}
.cover-divider{left:199px;top:468px;width:1px;height:28px;background:rgba(255,255,255,.7)}

/* intro */
.intro-brand{left:0;right:0;top:22px;text-align:center;font-family:var(--head);font-weight:600;font-size:22px;color:#4a4a4a;letter-spacing:1px}
.intro-brand small{display:block;font-size:8px;letter-spacing:3px;color:#4a4a4a;margin-top:1px}
.partner-bar{left:0;top:80px;width:378px;height:27px;background:var(--orange);display:flex;align-items:center;color:var(--white);font-family:var(--head);font-weight:600;font-size:10.5px}
.partner-bar span{flex:1;text-align:center}
.partner-bar .sep{flex:none;width:2px;height:16px;background:var(--green)}
.intro-photo{left:0;top:107px;width:378px;height:260px;background:linear-gradient(135deg,#8a5a3a 0%,#c69a78 45%,#e8dccd 100%)}
.intro-panel{left:0;top:365px;width:378px;height:140px;background:var(--orange)}
.intro-title{left:0;right:0;top:380px;text-align:center;color:var(--white);font-family:var(--head);font-weight:700;font-size:27px;line-height:1}
.intro-sub{left:0;right:0;top:412px;text-align:center;color:var(--white);font-family:var(--head);font-weight:500;font-size:17px;line-height:1.2}
.intro-copy{left:29px;right:25px;top:444px;color:var(--white);font-size:7px;font-weight:700;line-height:1.45;text-align:justify}
.intro-copy p+p{margin-top:6px}
.intro-url{left:0;right:0;top:507px;text-align:center;font-weight:700;font-size:12px;color:#3a3a3a}

/* expertise */
.tile{position:absolute}
.t1{left:0;top:0;width:186px;height:108px;background:linear-gradient(135deg,#f4f4f4,#c9ccd1)}
.t2{left:189px;top:0;width:189px;height:114px;background:linear-gradient(135deg,#e7c54a,#bfcfc6)}
.t3{left:0;top:111px;width:186px;height:112px;background:linear-gradient(135deg,#f0cf4f,#cfe0d6)}
.t4{left:189px;top:117px;width:189px;height:106px;background:radial-gradient(circle at 60% 55%,#3aa0ff 0%,#123a66 45%,#0b1e36 100%)}
.offer-box{left:0;top:227px;width:182px;height:149px;background:var(--orange);padding:18px 8px 0 14px;color:var(--white);font-family:var(--cond);font-weight:400;font-size:9.6px;line-height:1.6;list-style:none;text-align:justify}
.offer-box li{position:relative;padding-left:16px;margin-bottom:13px}
.offer-box li::before{content:"";position:absolute;left:0;top:3px;width:8px;height:8px;border-radius:50%;background:var(--green-soft)}
.sec-head{position:absolute;font-family:var(--head);font-weight:600;color:var(--orange-ink);font-size:11px;display:flex;align-items:center;gap:6px;line-height:1.2}
.sec-head .glyph{width:12px;height:12px;flex:none}
.ticks{position:absolute;list-style:none;font-size:6.8px;line-height:1.3;color:#333;text-align:justify}
.ticks li{position:relative;padding-left:10px;margin-bottom:6.5px}
.ticks li::before{content:"";position:absolute;left:0;top:1.5px;width:5px;height:5px;border-radius:50%;background:var(--green)}
.rule{left:199px;top:404px;width:164px;height:1.5px;background:var(--orange)}
.closing-note{left:207px;top:412px;width:156px;font-weight:700;color:var(--orange-ink);font-size:8px;line-height:1.3;text-align:justify}
.footer-wave{position:absolute;left:0;bottom:0;width:378px;height:70px}
.footer-url{position:absolute;left:0;right:0;bottom:20px;text-align:center;color:var(--white);font-weight:700;font-size:12.5px}

/* why */
.why-photo{left:0;top:0;width:155px;height:490px;background:linear-gradient(180deg,#f6f3ee 0%,#e2d8cc 45%,#7d7468 75%,#4a443d 100%)}
</style>
</head>
<body>
<main class="spread">

  <!-- Cover -->
  <section class="page p-cover">
    <div class="photo cover-photo" role="img" aria-label="Orange-toned close-up of an electric motor stator with copper windings"></div>
    <div class="abs brand-main">KELVORA THERMAL<small>SOLUTIONS</small></div>
    <div class="abs brand-second"><i></i>Veltrion</div>
    <p class="abs contact-lead"><b>FOR FURTHER INFORMATION</b><br><b>about how we can help you, please contact:</b></p>
    <ul class="abs contact-list mail">
      <li><span class="ic"></span>k.hollwedt@veltrion.com</li>
      <li><span class="ic"></span>m.ardley@thermalis-drives.co.uk</li>
    </ul>
    <div class="abs cover-divider"></div>
    <ul class="abs contact-list web">
      <li><span class="ic globe"></span>www.veltrion.com</li>
      <li><span class="ic globe"></span>www.thermalis-drives.co.uk</li>
    </ul>
  </section>

  <!-- Intro -->
  <section class="page p-intro">
    <div class="abs intro-brand">KELVORA THERMAL<small>SOLUTIONS</small></div>
    <div class="abs partner-bar"><span>VELTRION GMBH</span><i class="sep"></i><span>THERMALIS DRIVES LTD</span></div>
    <div class="photo intro-photo" role="img" aria-label="Team of engineers shaking hands over a desk with drawings"></div>
    <svg class="abs" style="left:0;top:330px" width="378" height="40" viewBox="0 0 378 40" aria-hidden="true">
      <path d="M0 40 V22 C90 -2 200 -4 378 8 V40Z" fill="var(--green)"/>
      <path d="M0 40 V30 C100 8 220 6 378 22 V40Z" fill="var(--white)"/>
      <path d="M0 40 V34 C100 14 220 12 378 26 V40Z" fill="var(--orange)"/>
    </svg>
    <div class="abs intro-panel"></div>
    <h1 class="abs intro-title">A PARTNERSHIP OF</h1>
    <h2 class="abs intro-sub">ELECTRICAL MACHINE DESIGN SPECIALISTS</h2>
    <div class="abs intro-copy">
      <p>Two complementary specialist companies working together to provide state-of-the art complete designs for electrical machines</p>
      <p>Located in Germany and UK, we are two complimentary electrical machines design companies, combining to provide electrical machine design services.</p>
    </div>
    <div class="abs intro-url">www.veltrion.com</div>
  </section>

  <!-- Expertise -->
  <section class="page p-expertise">
    <div class="tile t1" role="img" aria-label="Hand using a tablet over technical drawings"></div>
    <div class="tile t2" role="img" aria-label="Gears engraved with innovation and engineering"></div>
    <div class="tile t3" role="img" aria-label="Gears engraved with engineering and preparing"></div>
    <div class="tile t4" role="img" aria-label="Glowing blue electrical coil on a dark digital background"></div>
    <ul class="abs offer-box">
      <li>We offer full electrical machine design, from the concept stage to a full set of technical drawings and manufacturing documents</li>
      <li>We also offer modifications and improvements to existing electrical machine product ranges</li>
    </ul>
    <h3 class="sec-head" style="left:196px;top:232px">
      <svg class="glyph" viewBox="0 0 12 12" aria-hidden="true"><circle cx="5" cy="2.5" r="1.8" fill="none" stroke="var(--orange)" stroke-width="1.2"/><path d="M5 4 L1 11 M5 4 L9 11" stroke="var(--orange)" stroke-width="1.2" fill="none"/></svg>
      Specific design expertise include:
    </h3>
    <ul class="ticks" style="left:199px;top:253px;width:166px">
      <li>High Efficiency designs : up to 98.2% (10MW)</li>
      <li>Thermal management solutions for increased power density, reduced costs and increased product lifetime</li>
      <li>Design optimisation for technical specifications: cost, weight and manufacturability</li>
      <li>Robust vibration proven designs: up to 30 year lifetime</li>
      <li>Modular approach</li>
      <li>Validation plans &amp; test data evaluation for mechanical, electrical and thermal performance</li>
      <li>Root cause analysis – failure investigation</li>
    </ul>
    <div class="abs rule"></div>
    <p class="abs closing-note">Our highly skilled engineers work closely with customers to deliver designs according to set specification</p>
    <h3 class="sec-head" style="left:15px;top:391px">
      <svg class="glyph" viewBox="0 0 12 12" aria-hidden="true"><circle cx="6" cy="3" r="2" fill="var(--orange)"/><circle cx="2" cy="4" r="1.4" fill="var(--orange)"/><circle cx="10" cy="4" r="1.4" fill="var(--orange)"/><path d="M2 12 Q6 4 10 12Z" fill="var(--orange)"/></svg>
      We are experienced in:
    </h3>
    <ul class="ticks" style="left:18px;top:414px;width:170px">
      <li>Synchronous machines</li>
      <li>Induction machines, including Doubly Fed Induction Generators (DFIG)</li>
      <li>Permanent Magnet machines</li>
    </ul>
    <svg class="footer-wave" viewBox="0 0 378 70" preserveAspectRatio="none" aria-hidden="true">
      <path d="M0 20 C120 -4 260 0 378 8 V70 H0Z" fill="var(--green)"/>
      <path d="M0 26 C120 4 260 8 378 22 V70 H0Z" fill="var(--white)"/>
      <path d="M0 30 C120 10 260 14 378 28 V70 H0Z" fill="var(--orange)"/>
    </svg>
    <div class="footer-url">www.veltrion.com</div>
  </section>

  <!-- Why work with us -->
  <section class="page p-why">
    <div class="photo why-photo" role="img" aria-label="Engineer marking a technical drawing of an electrical machine"></div>
    <h3 class="sec-head" style="left:164px;top:22px">
      <svg class="glyph" viewBox="0 0 12 12" aria-hidden="true"><rect x="1" y="3.5" width="10" height="7.5" rx="1" fill="var(--orange)"/><rect x="4" y="1.5" width="4" height="2.5" fill="none" stroke="var(--orange)" stroke-width="1"/></svg>
      Why work with us?
    </h3>
    <ul class="ticks" style="left:170px;top:50px;width:197px">
      <li>A complete package: Electromagnetic Design, Mechanical Design, Thermal Design &amp; Manufacturing engineering</li>
      <li>Extensive application experience: Marine, stationary power plant, industrial, oil/gas offshore, hydro, wind</li>
      <li>Machine designs with world best efficiency (98.2% at 10MW)</li>
      <li>Robust designs withstanding high vibration levels – e.g. driven by gas / diesel engines for up to 30 year lifetime</li>
      <li>Modular approach, integrated product design and serial product knowledge: parts reduced by up to 75%</li>
      <li>Comprehensive validation program using in depth Multiphysics FEA simulations to prove detailed test data</li>
      <li>Advanced modelling software, customised for electrical machine analysis</li>
    </ul>
    <h3 class="sec-head" style="left:164px;top:231px">
      <svg class="glyph" viewBox="0 0 12 12" aria-hidden="true"><path d="M0 5 L4 3 L8 5 L12 3 V7 L8 9 L4 7 L0 9Z" fill="var(--orange)"/></svg>
      Our experiences
    </h3>
    <ul class="ticks" style="left:170px;top:261px;width:197px">
      <li>Pool of specialists with more than 150 years of combined experience in Electrical Machine Design: Electromagnetic, Mechanical, Thermal &amp; Manufacturing</li>
      <li>Extensive experience cutting across industry and academia</li>
      <li>Experience working with companies including Norvant, Halbeck, Corvantis, Brenmoor and University of Eastfield Electrical Machines Department</li>
      <li>R&amp;D experiences of conventional and novel electrical machines, including simulation and implementation of novel thermal solutions</li>
      <li>5 commercial products developed - from concept via prototype to serial production</li>
      <li>Up to 20MW; 400V – 15kV</li>
      <li>500rpm – 1800rpm</li>
      <li>Up to 80 tons</li>
      <li>International customer base</li>
    </ul>
    <svg class="footer-wave" viewBox="0 0 378 70" preserveAspectRatio="none" aria-hidden="true">
      <path d="M0 20 C120 -4 260 0 378 8 V70 H0Z" fill="var(--green)"/>
      <path d="M0 26 C120 4 260 8 378 22 V70 H0Z" fill="var(--white)"/>
      <path d="M0 30 C120 10 260 14 378 28 V70 H0Z" fill="var(--orange)"/>
    </svg>
    <div class="footer-url">www.veltrion.com</div>
  </section>

</main>
</body>
</html>
```